Website for Sports and Exercise Medicine Doctor with active research in stem cells therapies.

I am a sports and exercise medicine doctor with research interests in the cutting edge areas of biological therapies, most notable stem cells. None of my patients are dying of anything, and most of them come to see me to decrease their pain, so they can get back to what they want to do.

The approach i then take is to decrease their pain and support them to achieve the things they wish to achieve. Most people start at "Just make it stop hurting doc" , but I try to move them towards something more important over time.

I would like the website to be very different to other "Doctor or medical websites" in its look. No pictures of doctors in white coats and no pictures of fit old people smiling. I would potentially like the fist thing seen to be a quote:

"Less pain. Everybody wants it, but what are you going to do, once you've got it?"

(But this is only an idea, I am open to anything)

The website will need a couple of things

1. "Locations" I work
2. "Research" I am involved in
3. "Sort Me out" - Clinical information for people to access
4. "Social" - imbedded twitter and facebook
5. "Blog" - imbedded wordpress blog
6. "Bio" - the usual bio-stuff

The "Sort Me out" - pages I would like to have the functionality as seen in this site http://www.veltarion.com.au/platelet/. I intend to put disease topics into these pages (eg Achilles tehdinopathy, osteoarthritis etc etc etc). Once again I am not wedded to this but something along these lines would be good.

To give you an idea these are some sites I like
http://www.morbanquilt.com/
http://daptrine.com/
http://ovimbera.com.sg/
http://jolvaniketchup.com/
http://www.pilnorwave.com/
http://quadrisel.com/#offering
http://fennikstudio.tv/
http://norvalgate.com/
http://sablethorn.co.uk/#about

Target Market(s)

20-80 year old.
People with tendon injuries
People with osteoarthritis
People interested in stem cells
I will build the site over time to contain information on multiple sporting injuries and musculoskeletal disorders. It will also become a site for the latest on stem cell research particularly in the area of osteoarthritis.

Industry/Entity Type

Medical

Font styles to use
Sans Serif

Colors
ffffff

Requirements
Nice to have
• To give you an idea these are some sites I like
http://daptrine.com/
http://fennikstudio.tv/
http://norvalgate.com/
Should not have
• Pictures of doctors in white coats or old fit people smiling

```html
<!DOCTYPE html>
<html lang="en">
<head>
<meta charset="utf-8">
<title>Dr Owen Hartley – Sports and Exercise Medicine</title>
<link rel="stylesheet" href="https://fonts.googleapis.com/css2?family=Open+Sans:wght@400;600;700&family=Raleway:wght@300;400;500&display=swap">
<style>
  :root {
    --blue: #2aa6dc;
    --blue-dark: #1c86b8;
    --ink: #3d3d3d;
    --text: #5a5a5a;
    --muted: #8a8a8a;
    --grey-band: #ecebe8;
    --quote-bg: #f6f3e6;
    --quote-border: #dcd7c2;
    --footer: #2a2a2a;
    --white: #ffffff;
  }
  * { box-sizing: border-box; margin: 0; padding: 0; }
  html, body { width: 1200px; height: 2804px; overflow: hidden; }
  body {
    background: var(--white);
    font-family: "Open Sans", Arial, sans-serif;
    color: var(--text);
    position: relative;
  }

  /* Hero */
  .hero {
    position: absolute; left: 0; top: 0; width: 1200px; height: 780px;
    background:
      linear-gradient(180deg, rgba(20,14,10,0) 70%, rgba(20,14,10,.95) 100%),
      linear-gradient(180deg, #2a1a12 0%, #6b2a10 18%, #c4520f 38%, #f09a1c 55%, #f5c03a 63%, #c85a12 74%, #3a1c0c 88%, #1b120c 100%);
  }
  .site-header {
    position: absolute; left: 0; top: 0; width: 1200px; height: 110px;
    display: flex; align-items: center; justify-content: space-between;
    padding: 0 80px 0 110px;
  }
  .brand {
    font-family: "Raleway", sans-serif; font-weight: 300;
    font-size: 34px; color: var(--white); letter-spacing: 1px;
  }
  .main-nav { display: flex; gap: 10px; }
  .main-nav a {
    font-family: "Open Sans", sans-serif; font-size: 17px; color: var(--white);
    text-decoration: none; padding: 6px 14px;
  }
  .main-nav a.is-active { background: var(--blue); }
  .hero-quote {
    position: absolute; left: 0; top: 262px; width: 1200px; text-align: center;
    font-family: "Open Sans", sans-serif; font-weight: 700;
    font-size: 50px; line-height: 64px; color: var(--white);
  }
  .hero-button {
    position: absolute; left: 470px; top: 520px; width: 270px; height: 66px;
    background: linear-gradient(180deg, #45b8ea, var(--blue-dark));
    border-radius: 8px; color: var(--white); font-size: 27px;
    display: flex; align-items: center; justify-content: center;
  }

  /* Welcome */
  .welcome { position: absolute; left: 0; top: 780px; width: 1200px; height: 250px; }
  .welcome h1 {
    position: absolute; left: 130px; top: 30px;
    font-family: "Raleway", sans-serif; font-weight: 400; font-size: 38px; color: var(--blue);
  }
  .welcome p {
    position: absolute; left: 130px; top: 92px; width: 640px;
    font-size: 16px; line-height: 25px; color: var(--text);
  }
  .welcome .read-more {
    position: absolute; left: 130px; top: 200px; font-size: 15px; color: var(--blue);
  }
  .portrait {
    position: absolute; left: 822px; top: 24px; width: 204px; height: 204px;
    border-radius: 50%; border: 6px solid var(--white);
    box-shadow: 0 0 0 2px #cfcfcf;
    background: radial-gradient(circle at 50% 40%, #c98c6a, #6a4634 70%, #2f2a2a);
  }

  /* Services */
  .services {
    position: absolute; left: 0; top: 1032px; width: 1200px; height: 510px;
    background: var(--grey-band);
  }
  .service { position: absolute; width: 330px; text-align: center; }
  .service h2 {
    font-family: "Raleway", sans-serif; font-weight: 400; font-size: 32px; color: var(--blue);
    margin-bottom: 18px;
  }
  .service p { font-size: 15px; line-height: 23px; color: var(--text); }

  /* Testimonials */
  .testimonials { position: absolute; left: 0; top: 1560px; width: 1200px; height: 500px; }
  .testimonials > h2 {
    position: absolute; left: 0; top: 36px; width: 1200px; text-align: center;
    font-family: "Raleway", sans-serif; font-weight: 400; font-size: 44px; color: var(--blue);
  }
  .testimonial { position: absolute; top: 116px; width: 290px; text-align: center; }
  .testimonial .avatar {
    width: 128px; height: 128px; margin: 0 auto; border-radius: 50%;
    border: 5px solid var(--white); box-shadow: 0 0 0 2px #d2d2d2;
  }
  .testimonial h3 {
    margin-top: 14px; font-family: "Raleway", sans-serif; font-weight: 500;
    font-size: 24px; color: var(--blue);
  }
  .testimonial .role { font-size: 13px; color: var(--muted); margin-top: 2px; }
  .testimonial blockquote {
    margin-top: 22px; background: var(--quote-bg); border: 1px solid var(--quote-border);
    box-shadow: 0 3px 6px rgba(0,0,0,.12); padding: 18px 20px;
    font-size: 14px; line-height: 22px; color: var(--text);
  }

  /* Contact */
  .contact {
    position: absolute; left: 0; top: 2060px; width: 1200px; height: 580px;
    background: var(--grey-band);
  }
  .contact h2 {
    position: absolute; left: 0; top: 60px; width: 1200px; text-align: center;
    font-family: "Raleway", sans-serif; font-weight: 400; font-size: 46px; color: var(--blue);
  }
  .contact .intro {
    position: absolute; left: 200px; top: 132px; width: 800px;
    font-size: 18px; line-height: 30px; color: var(--ink);
  }
  .contact .intro span { color: var(--blue); }
  .field {
    position: absolute; background: var(--white); border: 1px solid #cfcfcf;
    font-size: 14px; color: #a5a5a5; padding: 12px 14px;
  }
  .submit {
    position: absolute; left: 200px; top: 2564px; width: 250px; height: 52px;
    background: var(--blue); color: var(--white); font-size: 26px;
    display: flex; align-items: center; justify-content: center;
  }

  /* Footer */
  .site-footer {
    position: absolute; left: 0; top: 2640px; width: 1200px; height: 164px;
    background: var(--footer);
  }
  .site-footer .copyright {
    position: absolute; left: 140px; top: 70px; font-size: 16px; color: #d8d8d8;
  }
  .social { position: absolute; left: 880px; top: 48px; display: flex; gap: 28px; }
  .social span { width: 68px; height: 68px; border-radius: 50%; background: var(--blue); display: block; }
</style>
</head>
<body>

<section class="hero" role="img" aria-label="Silhouettes of runners against a bright orange sunset">
</section>

<header class="site-header">
  <div class="brand">Dr Owen Hartley</div>
  <nav class="main-nav">
    <a href="#">Locations</a>
    <a href="#">Research</a>
    <a href="#" class="is-active">Sort Me Out</a>
    <a href="#">Social</a>
    <a href="#">Blog</a>
    <a href="#">Bio</a>
  </nav>
</header>

<p class="hero-quote">Less pain. Everybody wants it, but what are<br>you going to do, once you’ve got it?</p>
<a class="hero-button">Learn More</a>

<section class="welcome">
  <h1>welcome to Dr Owen Hartley</h1>
  <p>I help active people reduce their pain and return to the things they love. My clinical work combines sports and exercise medicine with research into biological therapies, including stem cells, so each treatment plan looks beyond the next appointment toward your longer term goals.</p>
  <a class="read-more">Read More &nbsp;›</a>
  <div class="portrait" role="img" aria-label="Portrait photo of the doctor"></div>
</section>

<section class="services">
  <div class="service" style="left:135px; top:100px;">
    <h2>Tendon Injuries</h2>
    <p>Achilles, patellar and shoulder tendon problems can linger for months. Learn what loads help healing, which treatments have evidence behind them and how to plan a steady return.</p>
  </div>
  <div class="service" style="left:735px; top:100px;">
    <h2>Osteoarthritis</h2>
    <p>Stiff and painful joints do not have to end an active life. Find out how exercise, weight, injections and newer biological options can keep you moving for longer.</p>
  </div>
  <div class="service" style="left:135px; top:300px;">
    <h2>Stem Cells</h2>
    <p>Stem cell therapy is a fast moving field. Read clear summaries of the latest studies, what they mean for joints and tendons, and where the real limits still are.</p>
  </div>
  <div class="service" style="left:735px; top:300px;">
    <h2>Sporting Injuries</h2>
    <p>From running knees to rolled ankles, sporting injuries need a plan. Get practical advice on rest, rehab and when to seek help so you can get back in the game.</p>
  </div>
</section>

<section class="testimonials">
  <h2>Some Kind Words from Our Awesome Clients</h2>
  <div class="testimonial" style="left:130px;">
    <div class="avatar" role="img" aria-label="Client photo" style="background:radial-gradient(circle at 50% 40%, #b5634a, #5a2c22);"></div>
    <h3>Nadia Brooks</h3>
    <div class="role">Distance Runner</div>
    <blockquote>After years of sore knees I finally have a plan that works. I am running again and enjoying every kilometre of it.</blockquote>
  </div>
  <div class="testimonial" style="left:455px;">
    <div class="avatar" role="img" aria-label="Client photo" style="background:radial-gradient(circle at 50% 40%, #d0a486, #6b5546);"></div>
    <h3>Pieter Vandermolen</h3>
    <div class="role">Weekend Cyclist</div>
    <blockquote>Clear advice, honest answers and real results. My shoulder is stronger than it has been in a decade of riding.</blockquote>
  </div>
  <div class="testimonial" style="left:780px;">
    <div class="avatar" role="img" aria-label="Client photo" style="background:radial-gradient(circle at 50% 40%, #d9a078, #8a5a38);"></div>
    <h3>Fiona Castleby</h3>
    <div class="role">Tennis Player</div>
    <blockquote>I came in wanting the pain gone and left with goals I never expected. Thank you for the patience and care.</blockquote>
  </div>
</section>

<section class="contact">
  <h2>Let’s Start The Conversation</h2>
  <p class="intro">If you’re looking to start working with us, then fill out the form below and we’ll be in contact shortly. Don’t be shy. For all other enquiries, including collaborations email: <span>info@drowenhartley.com.au</span></p>
</section>
<div class="field" style="left:200px; top:2296px; width:250px; height:46px;">Name</div>
<div class="field" style="left:470px; top:2296px; width:250px; height:46px;">Phone No</div>
<div class="field" style="left:740px; top:2296px; width:250px; height:46px;">Email</div>
<div class="field" style="left:200px; top:2364px; width:790px; height:176px;">Message</div>
<a class="submit">Submit</a>

<footer class="site-footer">
  <p class="copyright">© 2013, All Rights Reserved</p>
  <div class="social"><span aria-label="Social profile"></span><span aria-label="Social profile"></span></div>
</footer>

</body>
</html>
```